BrookhavenLLC

Real Estate Investment. Buy/Sell house/investment . Trustworthy,Reliable, and friendly

Industry/Entity Type

Real Estate

Contact Information for Business Card

Brookhaven@mailbox-example.com
808-555-0143
Linnea-Joy Patterson

```html
<!DOCTYPE html>
<html lang="en">
<head>
<meta charset="utf-8">
<title>Brookhaven LLC — Business Card</title>
<link rel="stylesheet" href="https://fonts.googleapis.com/css2?family=Cinzel:wght@400;500&family=Arimo:wght@400&display=swap">
<style>
  :root {
    --backdrop: #4b464b;
    --card-black: #050505;
    --text-white: #f2f2f2;
    --text-soft: #e4e4e4;
    --art-red: #6e2a22;
    --art-green: #9aa58c;
    --art-grey: #5d5d5d;
  }
  html, body {
    margin: 0;
    padding: 0;
    width: 1200px;
    height: 960px;
    overflow: hidden;
    background: var(--backdrop);
  }
  .canvas {
    width: 1200px;
    height: 960px;
    display: flex;
    align-items: center;
    justify-content: center;
  }
  .business-card {
    position: relative;
    width: 480px;
    height: 820px;
    background: var(--card-black);
    border-radius: 26px;
    box-shadow: 0 18px 40px rgba(0,0,0,0.45);
    color: var(--text-white);
    text-align: center;
  }
  .company-block {
    position: absolute;
    top: 132px;
    left: 0;
    right: 0;
  }
  .company-name {
    font-family: "Cinzel", serif;
    font-weight: 400;
    font-size: 34px;
    letter-spacing: 1px;
    margin: 0 0 6px;
  }
  .tagline {
    font-family: "Arimo", sans-serif;
    font-size: 23px;
    line-height: 1.15;
    color: var(--text-soft);
    margin: 0;
  }
  .person-name {
    position: absolute;
    top: 290px;
    left: 0;
    right: 0;
    font-family: "Arimo", sans-serif;
    font-size: 25px;
    line-height: 1.2;
    margin: 0;
  }
  .contact-list {
    position: absolute;
    top: 398px;
    left: 0;
    right: 0;
    font-family: "Arimo", sans-serif;
    font-size: 23px;
    line-height: 1.25;
    margin: 0;
    padding: 0;
    list-style: none;
  }
  .house-art {
    position: absolute;
    top: 500px;
    left: 70px;
    width: 280px;
    height: 220px;
    border-radius: 50% 50% 46% 46%;
    background:
      radial-gradient(ellipse at 55% 40%, var(--art-red) 0%, #4a1e19 38%, transparent 62%),
      radial-gradient(ellipse at 50% 60%, var(--art-green) 0%, var(--art-grey) 45%, transparent 72%);
    opacity: 0.9;
  }
</style>
</head>
<body>
  <main class="canvas">
    <article class="business-card">
      <header class="company-block">
        <h1 class="company-name">Brookhaven LLC</h1>
        <p class="tagline">Real Estate Investment</p>
        <p class="tagline">Buy/Sell house/investment</p>
      </header>
      <p class="person-name">Linnea<br>Joy Patterson</p>
      <ul class="contact-list">
        <li class="contact-phone">808-555-0143</li>
        <li class="contact-email">Brookhaven@mailbox-example.com</li>
      </ul>
      <div class="house-art" role="img" aria-label="Illustration of a red brick house sitting on a pile of dollar bills"></div>
    </article>
  </main>
</body>
</html>
```